Stonebay Towing Business Card

Towing
Accident towing
Mechanical breakdown
Insurance, salvage and recovery
4wd off road towing
Light & Heavy towing
8347 2516
24 hour business 7 days

Logo can be whole size on front

Industry/Entity Type

Towing/ transport

Contact Information for Business Card

The above

```html
<!DOCTYPE html>
<html lang="en">
<head>
<meta charset="utf-8">
<title>Stonebay Towing Business Card</title>
<link rel="stylesheet" href="https://fonts.googleapis.com/css2?family=Montserrat:wght@700;800&family=Fredoka:wght@600&display=swap">
<style>
  :root {
    --page: #ffffff;
    --yellow: #fbfb52;
    --black: #1b1b1b;
    --red: #d01f27;
    --pale-yellow: #f7f7a8;
    --pale-grey: #e6e6e6;
    --ink: #0d0d0d;
    --dimension: #3a78b0;
  }
  html, body {
    margin: 0;
    padding: 0;
    width: 1200px;
    height: 1200px;
    overflow: hidden;
    background: var(--page);
  }
  .sheet {
    position: relative;
    width: 1200px;
    height: 1200px;
  }
  .card {
    position: absolute;
    left: 277px;
    width: 642px;
    height: 392px;
    overflow: hidden;
  }
  .card-front { top: 177px; }
  .card-back { top: 648px; }
  .card-pattern {
    position: absolute;
    inset: 0;
  }
  .card-front .card-pattern {
    background: radial-gradient(circle at 84% 25%, var(--yellow) 0%, #d8d83c 35%, #7a7a2c 70%, #4a4a22 100%);
  }
  .card-back .card-pattern {
    background: radial-gradient(circle at 27% 55%, var(--pale-yellow) 0%, #efefc4 50%, var(--pale-grey) 100%);
  }
  .brand-name {
    position: absolute;
    left: 0;
    right: 0;
    top: 132px;
    margin: 0;
    text-align: center;
    font-family: "Montserrat", sans-serif;
    font-weight: 800;
    font-size: 56px;
    letter-spacing: -0.5px;
    color: var(--red);
  }
  .phone {
    position: absolute;
    left: 0;
    right: 0;
    top: 300px;
    margin: 0;
    text-align: center;
    font-family: "Fredoka", sans-serif;
    font-weight: 600;
    font-size: 70px;
    line-height: 1;
    color: var(--red);
    -webkit-text-stroke: 3px #ffffff;
    paint-order: stroke fill;
  }
  .services {
    position: absolute;
    left: 26px;
    top: 28px;
    margin: 0;
    padding: 0;
    list-style: none;
    font-family: "Montserrat", sans-serif;
    font-weight: 700;
    font-size: 32px;
    line-height: 49px;
    color: var(--ink);
  }
  .hours {
    position: absolute;
    left: 0;
    right: 0;
    top: 322px;
    margin: 0;
    padding-left: 28px;
    text-align: center;
    font-family: "Montserrat", sans-serif;
    font-weight: 700;
    font-size: 42px;
    line-height: 1;
    color: var(--red);
  }
  .dimensions {
    position: absolute;
    inset: 0;
    pointer-events: none;
  }
  .dimensions line { stroke: var(--dimension); stroke-width: 1; }
  .dimensions .arrow { fill: var(--dimension); }
  .dimensions text {
    fill: var(--dimension);
    font-family: Arial, Helvetica, sans-serif;
    font-size: 28px;
  }
</style>
</head>
<body>
<main class="sheet">
  <section class="card card-front">
    <div class="card-pattern" role="img" aria-label="Yellow and black sunburst rays radiating from the upper right"></div>
    <h1 class="brand-name">Stonebay Towing</h1>
    <p class="phone">8347 2516</p>
  </section>

  <section class="card card-back">
    <div class="card-pattern" role="img" aria-label="Pale yellow and light grey swirling sunburst rays"></div>
    <ul class="services">
      <li>Towing</li>
      <li>Accident towing</li>
      <li>Mechanical breakdown</li>
      <li>Insurance, salvage and recovery</li>
      <li>4wd off road towing</li>
      <li>Light &amp; Heavy towing</li>
    </ul>
    <p class="hours">24 hour business 7 days</p>
  </section>

  <svg class="dimensions" width="1200" height="1200" viewBox="0 0 1200 1200" aria-hidden="true">
    <!-- front width -->
    <line x1="277" y1="102" x2="277" y2="158"/>
    <line x1="919" y1="102" x2="919" y2="158"/>
    <line x1="277" y1="120" x2="555" y2="120"/>
    <line x1="642" y1="120" x2="919" y2="120"/>
    <polygon class="arrow" points="277,120 304,113 304,127"/>
    <polygon class="arrow" points="919,120 892,113 892,127"/>
    <text x="598" y="130" text-anchor="middle">3.54"</text>

    <!-- front height -->
    <line x1="212" y1="177" x2="259" y2="177"/>
    <line x1="212" y1="569" x2="259" y2="569"/>
    <line x1="229" y1="177" x2="229" y2="328"/>
    <line x1="229" y1="418" x2="229" y2="569"/>
    <polygon class="arrow" points="229,177 222,204 236,204"/>
    <polygon class="arrow" points="229,569 222,542 236,542"/>
    <text x="0" y="0" text-anchor="middle" transform="translate(239 373) rotate(-90)">2.17"</text>

    <!-- back height -->
    <line x1="937" y1="648" x2="996" y2="648"/>
    <line x1="937" y1="1041" x2="996" y2="1041"/>
    <line x1="978" y1="648" x2="978" y2="800"/>
    <line x1="978" y1="890" x2="978" y2="1041"/>
    <polygon class="arrow" points="978,648 971,675 985,675"/>
    <polygon class="arrow" points="978,1041 971,1014 985,1014"/>
    <text x="0" y="0" text-anchor="middle" transform="translate(988 845) rotate(-90)">2.17"</text>

    <!-- back width -->
    <line x1="277" y1="1070" x2="277" y2="1105"/>
    <line x1="919" y1="1070" x2="919" y2="1105"/>
    <line x1="277" y1="1088" x2="555" y2="1088"/>
    <line x1="642" y1="1088" x2="919" y2="1088"/>
    <polygon class="arrow" points="277,1088 304,1081 304,1095"/>
    <polygon class="arrow" points="919,1088 892,1081 892,1095"/>
    <text x="598" y="1098" text-anchor="middle">3.54"</text>
  </svg>
</main>
</body>
</html>
```